ZESTRO - Sydney Based Technology Consultancy -Logo & Business Card design

Who are we?
-
Zestro is an emerging and advanced technology consulting and professional services business based in Sydney, Australia. Zestro specialising in increasing value to organisations through the effective use of current and emerging technologies, ensuring that technology is a sustainable catalyst to attaining stated business goals.

We pride ourselves in challenging the norm.

What do we want?
-
We are looking to update our "Brand" we already have a simple “home grown” logo and we are now looking for a new one, once we have this updated logo and businesses look and feel though the business card design we will refresh our website with the new logo and design thus updating the Companies overall look at feel.

Our current site is www.zestro.net.au is a very basic wordpress site and we will be updating it once we have the new logo and designs done

Our initial thoughts on the new Zestro identity are
• Logo Concept
- One of the key things is obviously the 8
- I was thinking that a logo that had 8 as the core of the logo would be cool,
- Almost like having a “ring” or hoop that is twisted to form an 8 with different services scribed on the inside.
- So we would have a Large 8 and the inside would have ring each service or section engraved.

• Brand / web Feel
- Simple
- Professional
- Innovative
- Clear
- Destination
- Unique
- Impartial
- Safe
- Leading edge
- Familiar

- Emerging technologies
- White and ice / glacier blue
- The familiar feel of the Quillon web site
- Embedded specialist Video clips

• Portfolio of Services
- Zestro – A bright hub for bright minds
- Zestro – we supply the path to turn concepts from notion to outcome
- Focus should be on the brand quality consistent clear local knowledge with regional, national, theatre and global presence

Access to Specialists
- Emerging technologies
- Sustainability
- Collaboration
- Data centre
- Virtualisation

• Adjacent ideas under the one Brand
- Plexoro – Enable Business Collaboration
- Vantor – Infrastructure Virtualisation
- skolo - smart people and processes
- brevix - Emerging technologies
- maldoro - business to technology integration
- tessun - Smart Infrastructure
- wyn – Connected communities
- orba - sustainability

Target Market(s)

Australia, New Zealand and Asia pacific organisations that are typically English speaking.
Markets
- IT & Technology partners
- Banking and Finance
- Health

Industry/Entity Type

Business

Requirements
Must have
• Logo
Business cards
Colour pallette
3D Logo
Nice to have
• Style guide
Designer who can also assist with new Wordpress design
Should not have
• we don't want cheap looking, overtly flashy or gimmicky logo.

```html
<!DOCTYPE html>
<html lang="en">
<head>
<meta charset="utf-8">
<title>Zestro – Business Card</title>
<link rel="stylesheet" href="https://fonts.googleapis.com/css2?family=Arimo:wght@400;700&display=swap">
<style>
  :root {
    --page-bg: #e9ecef;
    --metal-light: #f4f5f6;
    --metal-mid: #d3d6d9;
    --metal-dark: #b5b9bd;
    --ink: #0d0d0d;
    --ice-blue: #3f9fe0;
    --card-shadow: rgba(0, 0, 0, 0.25);
  }
  * { margin: 0; padding: 0; box-sizing: border-box; }
  html, body {
    width: 1200px;
    height: 900px;
    overflow: hidden;
    background: var(--page-bg);
    font-family: "Arimo", Arial, sans-serif;
  }
  .canvas {
    width: 1200px;
    height: 900px;
    display: flex;
    flex-direction: column;
    align-items: center;
    justify-content: center;
    gap: 40px;
  }
  .card {
    position: relative;
    width: 640px;
    height: 391px;
    border-radius: 5px;
    background:
      repeating-linear-gradient(180deg, rgba(255,255,255,0.18) 0 2px, rgba(0,0,0,0.03) 2px 4px),
      linear-gradient(135deg, var(--metal-mid) 0%, var(--metal-light) 35%, var(--metal-dark) 60%, var(--metal-light) 85%, var(--metal-mid) 100%);
    box-shadow: 0 14px 36px var(--card-shadow);
    color: var(--ink);
    overflow: hidden;
  }

  /* Back side */
  .card-back {
    display: flex;
    align-items: center;
    justify-content: center;
    gap: 22px;
  }
  .back-mark {
    width: 150px;
    height: 150px;
    border-radius: 50%;
    background: var(--ice-blue);
  }
  .back-name {
    font-weight: 700;
    font-size: 58px;
    letter-spacing: 6px;
    color: var(--ice-blue);
  }

  /* Front side */
  .brand {
    position: absolute;
    left: 40px;
    top: 56px;
    display: flex;
    align-items: center;
    gap: 16px;
  }
  .brand-name {
    font-weight: 700;
    font-size: 94px;
    line-height: 1;
    letter-spacing: 8px;
  }
  .brand-mark {
    width: 78px;
    height: 78px;
    border-radius: 50%;
    background: var(--ice-blue);
  }
  .website {
    position: absolute;
    left: 44px;
    top: 164px;
    font-weight: 700;
    font-size: 14px;
  }
  .contact {
    position: absolute;
    right: 38px;
    bottom: 38px;
    text-align: right;
    line-height: 1.18;
  }
  .contact-name {
    font-weight: 700;
    font-size: 32px;
    letter-spacing: 1px;
    margin-bottom: 8px;
  }
  .contact-line { font-size: 18px; }
  .contact-email { font-weight: 700; font-size: 18px; }
  .contact-address { font-size: 16px; }
</style>
</head>
<body>
  <main class="canvas">
    <section class="card card-back" aria-label="Zestro business card, back">
      <span class="back-mark" aria-hidden="true"></span>
      <span class="back-name">ZESTRO</span>
    </section>
    <section class="card card-front" aria-label="Zestro business card, front">
      <div class="brand">
        <span class="brand-name">ZESTRO</span>
        <span class="brand-mark" aria-hidden="true"></span>
      </div>
      <p class="website">www.zestro.net.au</p>
      <div class="contact">
        <p class="contact-name">DANIEL HARCOURT</p>
        <p class="contact-line">+61 (0)400 555 123</p>
        <p class="contact-line">+61 (0)2 9000 4821</p>
        <p class="contact-email">daniel.harcourt@zestro.net.au</p>
        <p class="contact-address">suite 14, 210 Harbour Row, Sydney, NSW, 2000 Australia</p>
      </div>
    </section>
  </main>
</body>
</html>
```